CD Cover Design Project

Although I posted a picture as a possible idea, an idea from scratch is mostly what I am looking for. Definitely listen to the song before making the design. The link is posted right here in the project overview.
I need a CD cover for my latest single. This artwork will go up on Melodeck, brimora, etc with the song. Please listen to the song and then creat the artwork. Here is a link to the song:
http://tunevaultmusic.net/doriancolewhitfield/where-the-rivers-bend
The design needs my name, Dorian Cole Whitfield and it needs the song title, Where the Rivers Bend.
It needs to be a perfect square.
1600 by 1600
Resolution 300 DPI
Contact me at dorian@dorian-cole.net or (503) 482-3091

```html
<!DOCTYPE html>
<html lang="en">
<head>
<meta charset="utf-8">
<title>Where the Rivers Bend — Dorian Cole Whitfield</title>
<link rel="stylesheet" href="https://fonts.googleapis.com/css2?family=Black+Ops+One&family=Staatliches&family=Architects+Daughter&display=swap">
<style>
  :root {
    --page: #ffffff;
    --cover-dark: #140d08;
    --cover-deep: #0a0604;
    --stage-glow: #e9dcc0;
    --stage-mid: #8a7658;
    --stage-shadow: #2a1d13;
    --title-white: #f4f1ea;
    --name-orange: #f07a1c;
    --band: #050302;
  }
  * { box-sizing: border-box; margin: 0; padding: 0; }
  html, body {
    width: 1200px;
    height: 594px;
    overflow: hidden;
    background: var(--page);
  }
  .stage {
    position: relative;
    width: 1200px;
    height: 594px;
  }
  .cover {
    position: absolute;
    left: 320px;
    top: 17px;
    width: 560px;
    height: 560px;
    background: var(--cover-dark);
    overflow: hidden;
  }
  .cover__photo {
    position: absolute;
    left: 0;
    top: 110px;
    width: 560px;
    height: 420px;
    background:
      radial-gradient(ellipse 34% 40% at 52% 48%, var(--stage-glow) 0%, rgba(233,220,192,0.55) 35%, rgba(138,118,88,0) 75%),
      radial-gradient(ellipse 16% 60% at 20% 30%, rgba(233,220,192,0.45), rgba(233,220,192,0) 70%),
      radial-gradient(ellipse 16% 60% at 84% 30%, rgba(233,220,192,0.4), rgba(233,220,192,0) 70%),
      linear-gradient(to bottom, var(--stage-shadow) 0%, var(--stage-mid) 45%, var(--stage-shadow) 72%, var(--cover-deep) 100%);
    -webkit-mask-image: linear-gradient(to bottom, transparent 0%, #000 18%, #000 100%);
            mask-image: linear-gradient(to bottom, transparent 0%, #000 18%, #000 100%);
  }
  .cover__title {
    position: absolute;
    left: 0;
    width: 100%;
    text-align: center;
    color: var(--title-white);
  }
  .cover__title-lead {
    top: 28px;
    font-family: "Black Ops One", "Impact", sans-serif;
    font-size: 74px;
    line-height: 1;
    letter-spacing: 1px;
  }
  .cover__title-rest {
    top: 110px;
    font-family: "Staatliches", "Impact", sans-serif;
    font-size: 36px;
    line-height: 1;
    letter-spacing: 17px;
    padding-left: 17px;
  }
  .cover__band {
    position: absolute;
    left: 0;
    top: 458px;
    width: 100%;
    height: 58px;
    background: var(--band);
    border-top: 1px solid rgba(240,122,28,0.25);
    display: flex;
    align-items: center;
    justify-content: center;
  }
  .cover__artist {
    font-family: "Architects Daughter", cursive;
    font-size: 27px;
    color: var(--name-orange);
    letter-spacing: 1px;
  }
</style>
</head>
<body>
  <main class="stage">
    <section class="cover" aria-label="Single cover: Where the Rivers Bend by Dorian Cole Whitfield">
      <div class="cover__photo" role="img" aria-label="Concert photograph: band under warm stage spotlights with a crowd raising hands in silhouette"></div>
      <h1>
        <span class="cover__title cover__title-lead">WHERE</span>
        <span class="cover__title cover__title-rest">THE RIVERS BEND</span>
      </h1>
      <div class="cover__band">
        <p class="cover__artist">Dorian Cole Whitfield</p>
      </div>
    </section>
  </main>
</body>
</html>
```